Company Values Graphic

We are looking for a design of our company values that can be used in a variety of places including our website, mousepads, office posters, business cards, etc.

Notes:
- We'd rather have icons/art than photographs on the poster.... so more like an infographic
- The core value group headings are not required, but can be included if you think grouping the values works for your design
- We have a logo for our software product but that logo is not required
- We don't need/want clever images to accompany each value, but some images are fine
- BrisKel logo attached
- BrisKel colors are attached
- BrisKel logo is Nunito Sans ExtraBold 800
- BrisKel website uses Roboto

Our Values - Who we will work with (and who we will not)
The right set of values are essential to building and maintaining a culture that we all wake up eager to be a part of each day. They are foundational to all hiring and firing decisions. They attract the right people and repel the wrong ones.

BE HELPFUL
Make every person and place better because you are there.
Deliver wow with every interaction.

BE HUMBLE
Listen with every muscle.
Passionately help others first.
Seek first to understand.

BE HONEST
Earn trust every day.
Be open and direct.
Treat everyone with fairness and respect.

BE HUMAN
Celebrate passion and action.
Create an environment where people are authentic.
Hire great people and expect a lot from them

BE COURAGEOUS
Dare mighty things.
Make and honor commitments.
All great things start with a small act of courage applied at the right moment.

```html
<!DOCTYPE html>
<html lang="en">
<head>
<meta charset="utf-8">
<title>BrisKel Core Values</title>
<link href="https://fonts.googleapis.com/css2?family=Nunito+Sans:wght@700;800;900&family=Roboto:wght@100;400&display=swap" rel="stylesheet">
<style>
  :root {
    --bg: #ffd6d6;
    --yellow: #ffbf00;
    --orange: #ff3800;
    --red: #de0000;
    --ink: #111826;
  }
  * { margin: 0; padding: 0; box-sizing: border-box; }
  html, body { width: 927px; height: 1200px; overflow: hidden; background: var(--bg); }
  .poster { position: relative; width: 927px; height: 1200px; background: var(--bg); font-family: "Roboto", Arial, sans-serif; }

  .section-title {
    position: absolute; left: 56px; top: 48px;
    font-family: "Nunito Sans", Arial, sans-serif; font-weight: 800;
    font-size: 24px; letter-spacing: -0.03em; line-height: 1; color: var(--orange);
  }
  .title-rule { position: absolute; left: 223px; top: 62px; width: 646px; height: 2px; background: var(--yellow); }
  .corner-block { position: absolute; left: 868px; top: 45px; width: 59px; height: 33px; background: var(--orange); }

  .be {
    position: absolute; left: 48px;
    font-family: "Roboto", Arial, sans-serif; font-weight: 100;
    font-size: 240px; line-height: 1; letter-spacing: -0.06em;
  }
  .value-name {
    position: absolute; left: 300px;
    font-family: "Nunito Sans", Arial, sans-serif; font-weight: 900;
    font-size: 80px; line-height: 1; letter-spacing: -0.062em;
    white-space: nowrap;
  }
  .value-name.long { left: 294px; letter-spacing: -0.088em; }
  .value-rule { position: absolute; left: 298px; width: 498px; height: 2px; background: var(--orange); }
  .value-rule.long { width: 575px; }

  .point {
    position: absolute; font-size: 17px; line-height: 21.5px;
    color: var(--orange); letter-spacing: 0.01em;
  }
  .col-1 { left: 304px; }
  .col-2 { left: 458px; }
  .col-3 { left: 635px; }

  .value-icon { position: absolute; border-radius: 8px; }

  .yellow { color: var(--yellow); }
  .orange { color: var(--orange); }
  .red { color: var(--red); }

  .brand { position: absolute; left: 60px; top: 1104px; display: flex; align-items: center; gap: 12px; }
  .brand-dot { width: 44px; height: 44px; border-radius: 50%; background: var(--orange); }
  .brand-name {
    font-family: "Nunito Sans", Arial, sans-serif; font-weight: 800;
    font-size: 40px; line-height: 1; color: var(--ink); letter-spacing: -0.01em;
  }
  .footer-rule { position: absolute; left: 302px; top: 1127px; width: 625px; height: 3px; background: var(--orange); }
</style>
</head>
<body>
<main class="poster">
  <h1 class="section-title">CORE VALUES</h1>
  <div class="title-rule"></div>
  <div class="corner-block"></div>

  <!-- Helpful -->
  <span class="be yellow" style="top:75px">be</span>
  <h2 class="value-name yellow" style="top:165px">HELPFUL</h2>
  <div class="value-icon" role="img" aria-label="Icon of two people giving a high five" style="left:657px;top:149px;width:80px;height:75px;background:var(--orange)"></div>
  <div class="value-rule" style="top:240px"></div>
  <p class="point col-1" style="top:251px">Make every person and place<br>better because you are there.</p>
  <p class="point col-3" style="top:251px">Deliver wow with<br>every interaction</p>

  <!-- Humble -->
  <span class="be orange" style="top:264px">be</span>
  <h2 class="value-name orange" style="top:340px">HUMBLE</h2>
  <div class="value-icon" role="img" aria-label="Icon of a tree with roots below the ground" style="left:648px;top:327px;width:71px;height:78px;background:var(--red)"></div>
  <div class="value-rule" style="top:415px"></div>
  <p class="point col-1" style="top:428px">Listen with<br>every muscle</p>
  <p class="point col-2" style="top:428px">Passionately help<br>others first</p>
  <p class="point col-3" style="top:428px">Seek first to<br>understand</p>

  <!-- Honest -->
  <span class="be red" style="top:453px">be</span>
  <h2 class="value-name red" style="top:538px">HONEST</h2>
  <div class="value-icon" role="img" aria-label="Icon of four hands gripping each other's wrists" style="left:636px;top:526px;width:78px;height:69px;background:var(--yellow)"></div>
  <div class="value-rule" style="top:608px"></div>
  <p class="point col-1" style="top:620px">Earn trust<br>every day</p>
  <p class="point col-2" style="top:620px">Be open<br>and direct</p>
  <p class="point col-3" style="top:620px">Treat everyone with<br>fairness and respect</p>

  <!-- Human -->
  <span class="be yellow" style="top:642px">be</span>
  <h2 class="value-name yellow" style="top:717px">HUMAN</h2>
  <div class="value-icon" role="img" aria-label="Heart icon" style="left:633px;top:716px;width:70px;height:61px;background:var(--red)"></div>
  <div class="value-rule" style="top:791px"></div>
  <p class="point col-1" style="top:809px">Celebrate<br>passion<br>and action</p>
  <p class="point col-2" style="top:809px">Create an<br>environment<br>where people<br>are authentic</p>
  <p class="point col-3" style="top:809px">Hire great<br>people and<br>expect a lot<br>from them</p>

  <!-- Courageous -->
  <span class="be orange" style="top:831px">be</span>
  <h2 class="value-name long orange" style="top:924px">COURAGEOUS</h2>
  <div class="value-icon" role="img" aria-label="Icon of a climber raising a flag on a summit" style="left:824px;top:909px;width:46px;height:72px;background:var(--orange)"></div>
  <div class="value-rule long" style="top:993px"></div>
  <p class="point col-1" style="top:1007px">Dare mighty<br>things</p>
  <p class="point col-2" style="top:1007px">Make and<br>honor<br>commitments</p>
  <p class="point col-3" style="top:1007px">All great things<br>start with a small act<br>of courage applied<br>at the right moment</p>

  <footer class="brand">
    <span class="brand-dot"></span>
    <span class="brand-name">BrisKel</span>
  </footer>
  <div class="footer-rule"></div>
</main>
</body>
</html>
```